Unique Business Card Design

Unique Business Card design for our orthotic and prosthetic company. Our logo is on our website, color is light blue. Unique shape (artificial leg shaped, vertical, etc..) preferred. Logo, business name, individual name and basic demographics needed.

Industry/Entity Type

Business

Contact Information for Business Card

Logo, Industry, Phone # Logo, "Prosthetic & Orthotic Services" Place to add individual name and contact info

Colors
cee9f5

Requirements
Must have
• The icon must be there, placement of "Prosthetic & Orthotic Services" can be moved
Nice to have
• Like the mix of light blue, and a little darker blue. One design included the icons from my website which was a nice touch

```html
<!DOCTYPE html>
<html lang="en">
<head>
<meta charset="utf-8">
<title>LimbForm Inc. Business Card</title>
<link rel="stylesheet" href="https://fonts.googleapis.com/css2?family=Open+Sans:wght@700&family=Roboto:ital,wght@0,400;0,700;1,400&family=Crimson+Text:ital@1&display=swap">
<style>
  :root {
    --brand-blue: #245f95;
    --brand-blue-dark: #1f5687;
    --card-white: #f4f4f4;
    --text-dark: #2b2b2b;
    --text-mid: #3a3a3a;
    --band-dark: #3a3d3f;
    --divider: #d2d2d2;
    --page-bg: #e4e4e4;
    --white: #ffffff;
  }
  * { margin: 0; padding: 0; box-sizing: border-box; }
  html, body { width: 1200px; height: 576px; overflow: hidden; }
  body { background: var(--page-bg); position: relative; font-family: "Roboto", sans-serif; }

  .card {
    position: absolute;
    border-radius: 6px;
    overflow: hidden;
    box-shadow: 0 2px 4px rgba(0,0,0,0.25);
  }
  .card--front { left: 82px; top: 139px; width: 484px; height: 292px; background: linear-gradient(180deg, var(--brand-blue) 0%, var(--brand-blue-dark) 100%); }
  .card--back { left: 602px; top: 139px; width: 480px; height: 289px; background: var(--card-white); }

  .abs { position: absolute; white-space: nowrap; }

  .brand-mark { position: absolute; border-radius: 50%; }
  .card--front .brand-mark { left: 173px; top: 246px; width: 78px; height: 78px; background: var(--white); }
  .card--back .brand-mark { left: 72px; top: 68px; width: 86px; height: 86px; background: var(--brand-blue); }

  .brand-name { font-family: "Open Sans", sans-serif; font-weight: 700; letter-spacing: 0.3px; }
  .brand-rule { position: absolute; height: 2px; }
  .tagline { font-family: "Crimson Text", serif; font-style: italic; }

  .front-name { left: 189px; top: 107px; font-size: 22px; color: var(--white); }
  .front-rule { left: 189px; top: 137px; width: 203px; background: var(--white); }
  .front-tagline { left: 205px; top: 142px; font-size: 14px; color: var(--white); }
  .front-phone { left: 205px; top: 158px; font-size: 22px; font-weight: 700; color: var(--white); letter-spacing: 1px; }

  .back-name { left: 30px; top: 154px; font-size: 19px; color: var(--brand-blue); }
  .back-rule { left: 30px; top: 183px; width: 170px; background: var(--brand-blue); }
  .back-tagline { left: 48px; top: 186px; font-size: 13px; color: var(--brand-blue); }

  .divider { position: absolute; left: 223px; top: 41px; width: 1px; height: 184px; background: var(--divider); }

  .person-name { left: 245px; top: 53px; font-size: 20px; font-weight: 700; color: var(--brand-blue); }
  .person-role { left: 245px; top: 79px; font-size: 11.5px; font-style: italic; color: var(--text-mid); }

  .contact { left: 245px; display: flex; align-items: center; gap: 9px; color: var(--text-dark); }
  .contact svg { width: 11px; height: 11px; fill: var(--brand-blue-dark); flex: none; }
  .contact--mobile { top: 99px; font-size: 15px; }
  .contact--mobile svg { width: 12px; height: 14px; }
  .contact--phone { top: 135px; font-size: 13px; }
  .contact--fax { top: 153px; font-size: 13px; }
  .contact--email { top: 171px; font-size: 13px; }
  .address { left: 245px; top: 190px; font-size: 13px; color: var(--text-dark); }

  .band-dark { position: absolute; left: 0; bottom: 0; width: 210px; height: 19px; background: var(--band-dark); }
  .band-blue { position: absolute; right: 0; bottom: 0; width: 286px; height: 37px; background: var(--brand-blue); clip-path: polygon(20px 0, 100% 0, 100% 100%, 0 100%); }
  .website { right: 0; bottom: 0; left: auto; width: 286px; height: 37px; padding-left: 62px; line-height: 37px; font-size: 13px; color: var(--white); }
</style>
</head>
<body>

<section class="card card--front" aria-label="Card front">
  <span class="brand-mark" style="left:115px;top:107px;width:78px;height:78px;" aria-hidden="true"></span>
  <span class="abs brand-name front-name" style="left:207px;">LIMBFORM INC.</span>
  <span class="brand-rule front-rule" style="left:207px;"></span>
  <span class="abs tagline front-tagline" style="left:222px;">Prosthetic &amp; Orthotic Services</span>
  <span class="abs front-phone" style="left:230px;">555.204.1800</span>
</section>

<section class="card card--back" aria-label="Card back">
  <span class="brand-mark" aria-hidden="true"></span>
  <span class="abs brand-name back-name" style="left:38px;">LIMBFORM INC.</span>
  <span class="brand-rule back-rule"></span>
  <span class="abs tagline back-tagline">Prosthetic &amp; Orthotic Services</span>

  <span class="divider"></span>

  <span class="abs person-name">Talia Brenner</span>
  <span class="abs person-role">Orthotist/Prosthetist</span>

  <span class="abs contact contact--mobile">
    <svg viewBox="0 0 12 14"><path d="M2 0h8a1 1 0 0 1 1 1v12a1 1 0 0 1-1 1H2a1 1 0 0 1-1-1V1a1 1 0 0 1 1-1zm1 2v8h6V2zm3 9a1 1 0 1 0 0 2 1 1 0 0 0 0-2z"/></svg>
    555-3068142
  </span>
  <span class="abs contact contact--phone">
    <svg viewBox="0 0 12 12"><path d="M1 3c0-1 1-2 5-2s5 1 5 2v1H8V3H4v1H1zm2 2h6l2 2v4H1V7zm3 1.5a1.5 1.5 0 1 0 0 3 1.5 1.5 0 0 0 0-3z"/></svg>
    555.204.1800
  </span>
  <span class="abs contact contact--fax">
    <svg viewBox="0 0 12 12"><path d="M3 0h6v3H3zM1 4h10v5H9v3H3V9H1zm3 3v4h4V7z"/></svg>
    555.204.1819
  </span>
  <span class="abs contact contact--email">
    <svg viewBox="0 0 12 12"><path d="M6 0a6 6 0 1 0 0 12A6 6 0 0 0 6 0zm-1 1.2C4.3 2.2 4 3.5 3.9 5.5H1.3A4.8 4.8 0 0 1 5 1.2zm2 0a4.8 4.8 0 0 1 3.7 4.3H8.1C8 3.5 7.7 2.2 7 1.2zM5 5.5c.1-2 .5-3.3 1-4 .5.7.9 2 1 4zm-3.7 1h2.6c.1 2 .4 3.3 1.1 4.3A4.8 4.8 0 0 1 1.3 6.5zm3.7 0h2c-.1 2-.5 3.3-1 4-.5-.7-.9-2-1-4zm3.1 0h2.6A4.8 4.8 0 0 1 7 10.8c.7-1 1-2.3 1.1-4.3z"/></svg>
    tbrenner@limbforminc.com
  </span>
  <span class="abs address">2480 Harbor Ave. Brooklyn, NY 11229</span>

  <span class="band-dark"></span>
  <span class="band-blue"></span>
  <span class="abs website">www.limbforminc.com</span>
</section>

</body>
</html>
```